Vantro Baseball Athletic Training Brochure Design 3 Fold 8x8

I need to create a New 3 page folding brochure for an elite baseball training company that focuses on all aspects of becoming a better baseball player through athletic training. I would like it to be fresh and new. My client likes the Harbor City Comets colors. It needs to appeal to a young athletic crowd.

HERE IS A WEBSITE FROM A COMPETITOR
https://www.plinthrow.example/baseball/
I HAVE INCLUEDE A PDF FLYER OF SOMETHING THEIR COMPETITORS HAVE DONE

Target Market(s)

Professional and amateur baseball players

Font styles to use
Sans Serif

Colors
33a6d7
3176b5
000000
b2b2b2

Requirements
Must have
• Images featuring training. I would use KELBAFORM training images as well.
• References:
• "As a former professional baseball player, I know the hard work and dedication it takes to make it and be your best.
• Every athlete that aspires to be the best they can be must out work their opponents on all levels,
• especially when it comes to taking care of your body. Being strong physically is a must with all the
• elite athletes competing. To get an edge, you have to be on a program designed by en experienced trainer
• and leader. With that said, there's nobody I'd recommend higher than Dale Vantrock with Vantro's
• Training.
• -Corbin Pask
• Founder Hollow Birch Hitting
• 12 year Professional Veteran
• "Training at VT in the off-season had my body feeling the best it felt going into Spring Training. My power in hitting, my speed in running, and the quickness of my feet in the infield hadn’t felt this good in a long time."
• -Teodor Marquist, Professional Baseball Player
• "Dale is one of a handful of baseball-specific strength coaches that we choose to refer out to on the west coast when Halvik Motion Institute athletes are in search of quality supervision and an appreciation for the unique needs of this athletic population."
• Co-Owner of HMI, Gil Ostrander-
• "Having played at the professional level, I understand that the demands of the baseball season are tough and recovery is very important, but also realize the off-season is short and this not just a time to recover but get better."
• - Dale Vantrock Owner

```html
<!DOCTYPE html>
<html lang="en">
<head>
<meta charset="utf-8">
<title>Vantro's Training – Baseball Brochure</title>
<link href="https://fonts.googleapis.com/css2?family=Alfa+Slab+One&family=Oswald:wght@300;500;700&family=Lora:wght@400;600&family=Patrick+Hand&family=Montserrat:wght@600;800&display=swap" rel="stylesheet">
<style>
  :root {
    --page-bg: #e6e6e6;
    --blue-deep: #2453d4;
    --blue-mid: #3176b5;
    --blue-sky: #33a6d7;
    --cyan: #27d2ec;
    --ink: #1b1f2a;
    --white: #ffffff;
    --grey: #b2b2b2;
    --photo-dark: #1c3a7a;
    --photo-pink: #c9a3d8;
  }
  * { box-sizing: border-box; margin: 0; padding: 0; }
  html, body { width: 1200px; height: 798px; overflow: hidden; background: var(--page-bg); }
  body { position: relative; font-family: 'Lora', serif; }

  .panel {
    position: absolute; top: 211px; width: 375px; height: 375px; overflow: hidden;
    background: linear-gradient(160deg, var(--blue-deep) 0%, var(--blue-sky) 45%, var(--cyan) 100%);
    color: var(--white);
  }
  .panel--welcome { left: 15px; }
  .panel--testimonials { left: 390px; }
  .panel--cover { left: 795px; box-shadow: 0 6px 18px rgba(0,0,0,.25); }
  .spread-shadow { position: absolute; left: 15px; top: 211px; width: 750px; height: 375px; box-shadow: 0 6px 18px rgba(0,0,0,.25); }

  .abs { position: absolute; }
  .image-fill { position: absolute; }
  .crowd { left: 0; bottom: 0; width: 100%; height: 95px;
    background: linear-gradient(180deg, rgba(36,83,212,0) 0%, rgba(36,83,212,.55) 100%); }

  .brush { position: absolute; background: var(--white); transform: rotate(-18deg); }
  .name { font-family: 'Oswald', sans-serif; font-weight: 300; color: var(--blue-mid); font-size: 18px; line-height: 1; text-transform: uppercase; letter-spacing: .5px; white-space: nowrap; }
  .role { font-family: 'Montserrat', sans-serif; font-weight: 600; color: var(--ink); font-size: 6px; white-space: nowrap; }

  .badge { left: 168px; top: 34px; width: 46px; height: 46px; background: var(--white); border: 3px solid var(--ink); border-radius: 4px; }
  .welcome-title { left: 222px; top: 38px; font-family: 'Alfa Slab One', sans-serif; font-size: 18px; color: var(--ink); line-height: 1; white-space: nowrap; }
  .welcome-sub { left: 223px; top: 61px; font-family: 'Montserrat', sans-serif; font-weight: 600; font-size: 9.5px; letter-spacing: .4px; white-space: nowrap; }
  .body-copy { font-size: 6.6px; line-height: 1.45; color: var(--ink); }
  .body-copy p + p { margin-top: 5px; }
  .welcome-copy { left: 168px; top: 92px; width: 192px; }

  .stat { left: 28px; top: 258px; display: flex; align-items: flex-start; gap: 6px; }
  .stat-number { font-family: 'Oswald', sans-serif; font-weight: 700; font-size: 38px; line-height: .9; display: block; }
  .stat-unit { font-family: 'Oswald', sans-serif; font-size: 7px; display: block; }
  .stat-label { font-family: 'Oswald', sans-serif; font-weight: 300; font-size: 14px; line-height: 1.05; padding-top: 2px; }
  .quote-copy { left: 28px; top: 306px; width: 230px; color: var(--ink); }

  .slogan { left: 96px; top: 238px; font-family: 'Oswald', sans-serif; text-transform: uppercase; line-height: 1; }
  .slogan-line { display: block; font-size: 16px; }
  .slogan-bold { font-weight: 700; color: var(--ink); }
  .slogan-light { font-weight: 300; color: var(--ink); }
  .slogan-box { border: 2px solid var(--ink); padding: 3px 5px; margin-top: 4px; display: inline-block; }
  .slogan-box .slogan-line { font-size: 17px; }
  .slogan-box .slogan-bold { color: var(--white); }
  .owner-quote { left: 60px; top: 330px; width: 200px; font-family: 'Montserrat', sans-serif; font-weight: 600; font-size: 6px; line-height: 1.45; text-align: center; border-top: 1px solid var(--ink); padding-top: 5px; }

  .brand { left: 28px; top: 44px; display: flex; align-items: center; gap: 7px; }
  .brand-mark { width: 14px; height: 14px; background: var(--white); }
  .brand-name { font-family: 'Oswald', sans-serif; font-weight: 500; font-size: 18px; color: var(--white); text-transform: uppercase; }
  .plate { left: 92px; top: 95px; }
  .plate-text { left: 120px; top: 112px; width: 110px; text-align: center; font-family: 'Alfa Slab One', sans-serif; font-size: 24px; line-height: .92; color: var(--white); z-index: 2; }
  .headline { left: 88px; top: 176px; font-family: 'Alfa Slab One', sans-serif; font-size: 34px; line-height: .95; color: var(--ink);
    -webkit-text-stroke: 1px var(--white); z-index: 2; white-space: nowrap; }
  .tagline { left: 112px; top: 250px; width: 170px; text-align: center; font-family: 'Patrick Hand', sans-serif; font-size: 13px; line-height: 1.05; color: var(--ink); z-index: 2; }
  .batter-photo { left: 262px; top: 290px; width: 113px; height: 85px; background: linear-gradient(160deg,#7a2230,#d8d8e0); border-radius: 8px 0 0 0; z-index: 1; }
</style>
</head>
<body>
  <div class="spread-shadow"></div>

  <!-- Inside left panel -->
  <section class="panel panel--welcome">
    <div class="image-fill crowd" role="img" aria-label="Crowd silhouettes cheering"></div>
    <div class="image-fill" style="left:14px;top:40px;width:140px;height:140px;background:linear-gradient(180deg,var(--photo-pink),rgba(201,163,216,.25));opacity:.75;border-radius:6px;" role="img" aria-label="Faded silhouette of a batter in stance"></div>
    <div class="abs badge" role="img" aria-label="Academy badge"></div>
    <h1 class="abs welcome-title">WELCOME TO</h1>
    <p class="abs welcome-sub">VANTRO'S TRAINING</p>
    <div class="abs body-copy welcome-copy">
      <p>Every athlete that aspires to be the best they can be must out work their opponents on all levels, especially when it comes to taking care of your body.</p>
      <p>Once we have done the assessment, we can build a program of your individual goals and needs.</p>
      <p>Whether you want to take your sports performance to the next level or just feel better, get stronger, and lose body fat, Vantro's Training is for you.</p>
    </div>
    <div class="brush" style="left:22px;top:196px;width:140px;height:46px;" role="img" aria-label="White brush stroke"></div>
    <div class="abs" style="left:36px;top:203px;transform:rotate(-18deg);">
      <div class="name">Corbin Pask</div>
      <div class="role">Founder Hollow Birch Hitting</div>
    </div>
    <div class="abs stat">
      <div><span class="stat-number">12</span><span class="stat-unit">YEAR</span></div>
      <div class="stat-label">PROFESSIONAL<br>VETERAN</div>
    </div>
    <div class="abs body-copy quote-copy">
      <p>"Training at VT in the off-season had my body feeling the best it felt going into Spring Training. My power in hitting, my speed in running, and the quickness of my feet in the infield hadn't felt this good in a long time."</p>
      <p>Baseball was my passion, now my drive is helping athletes perform at the top of their game. I love watching my athletes take their results from the gym to their sport.</p>
    </div>
  </section>

  <!-- Inside right panel -->
  <section class="panel panel--testimonials">
    <div class="image-fill crowd" role="img" aria-label="Crowd silhouettes cheering"></div>
    <div class="image-fill" style="left:95px;top:0;width:130px;height:112px;background:linear-gradient(135deg,var(--photo-dark),var(--blue-sky));" role="img" aria-label="Photo of an athlete lifting dumbbells"></div>
    <div class="brush" style="left:222px;top:30px;width:145px;height:42px;" role="img" aria-label="White brush stroke"></div>
    <div class="abs" style="left:234px;top:36px;transform:rotate(-18deg);">
      <div class="name" style="font-size:15px;">Teodor Marquist</div>
      <div class="role">Professional Baseball Player</div>
    </div>
    <div class="brush" style="left:10px;top:165px;width:140px;height:46px;" role="img" aria-label="White brush stroke"></div>
    <div class="abs" style="left:22px;top:172px;transform:rotate(-18deg);">
      <div class="name" style="font-size:16px;">Dale Vantrock</div>
      <div class="role">Co-Owner</div>
    </div>
    <div class="image-fill" style="left:22px;top:232px;width:66px;height:88px;background:linear-gradient(180deg,#e8923a,#2a2a2a);border-radius:6px;" role="img" aria-label="Illustration of an athlete doing a box jump"></div>
    <div class="abs slogan">
      <span class="slogan-line slogan-bold">MOVE</span>
      <span class="slogan-line slogan-light">BETTER</span>
      <span class="slogan-box">
        <span class="slogan-line"><span class="slogan-bold">FEEL</span> <span class="slogan-light">BETTER</span></span>
        <span class="slogan-line"><span class="slogan-bold" style="color:var(--ink)">BE</span> <span class="slogan-light">BETTER</span></span>
      </span>
    </div>
    <p class="abs owner-quote">"As a former professional baseball player, I know the hard work and dedication it takes to make it and be your best."</p>
  </section>

  <!-- Front cover -->
  <section class="panel panel--cover">
    <div class="image-fill crowd" style="height:120px;" role="img" aria-label="Crowd silhouettes waving flags"></div>
    <div class="brand abs">
      <span class="brand-mark"></span>
      <span class="brand-name">Vantro's Training</span>
    </div>
    <svg class="abs plate" width="170" height="90" viewBox="0 0 170 90" aria-hidden="true">
      <polygon points="6,14 150,2 164,40 98,86 24,72" fill="var(--ink)"/>
      <polygon points="16,20 144,10 154,40 96,76 30,64" fill="var(--blue-mid)" stroke="var(--white)" stroke-width="2"/>
    </svg>
    <div class="abs plate-text">NEXT<br>UP</div>
    <h2 class="abs headline">BASEBALL<br>TRAINING</h2>
    <p class="abs tagline">Professional Training Tailored<br>for You!</p>
    <div class="image-fill batter-photo" role="img" aria-label="Photo of a batter mid-swing"></div>
  </section>
</body>
</html>
```